Website design: Mobile Physiotherapy, Massage & Personal Training Business

I need a website that reflects a staff of health and fitness professionals. I would like the theme of the website to match the company logo (Summit Motion Wellness).
This is a link for a competitors website that I am fond of:
http://www.brackenrehab.com.au/
I am open to any and all creative and innovative designs.

```html
<!DOCTYPE html>
<html lang="en">
<head>
<meta charset="utf-8">
<title>Summit Motion Wellness</title>
<link href="https://fonts.googleapis.com/css2?family=PT+Sans:wght@400;700&family=PT+Sans+Narrow:wght@400;700&family=Lora:ital,wght@1,700&display=swap" rel="stylesheet">
<style>
:root{
  --red:#b30a0f;
  --ink:#3a3a3a;
  --text:#222;
  --footer:#3b3b3b;
  --plate:#f4f4f4;
  --line:#c4161c;
}
*{margin:0;padding:0;box-sizing:border-box}
html,body{width:791px;height:1200px;overflow:hidden;background:#fff}
body{font-family:"PT Sans",sans-serif;color:var(--text);position:relative}
.abs{position:absolute}
.hero{left:0;top:0;width:791px;height:470px;background:linear-gradient(180deg,#dfe6e8 0%,#cbd5d1 25%,#8ea27a 55%,#5a7846 80%,#5f7a4a 100%)}
.logo-plate{left:95px;top:0;width:188px;height:72px;background:var(--plate);clip-path:polygon(8% 0,92% 0,100% 50%,92% 100%,8% 100%,0 50%);display:flex;align-items:center;justify-content:center}
.brand{font-weight:700;color:var(--red);font-size:15px;text-align:center;line-height:1.1}
.social{left:572px;top:0;width:110px;height:22px;background:var(--plate);clip-path:polygon(0 0,100% 0,88% 100%,6% 100%);display:flex;gap:10px;justify-content:center;align-items:center}
.social span{width:11px;height:11px;border-radius:50%;background:#8a8a8a}
.hours{left:435px;top:58px;width:258px;height:23px;background:var(--plate);clip-path:polygon(4% 0,96% 0,100% 100%,0 100%);font-size:8.5px;display:flex;align-items:center;justify-content:center;gap:3px;color:#333}
.hours a{color:var(--red);text-decoration:none}
.nav{left:94px;top:81px;width:602px;height:31px;background:linear-gradient(180deg,#d1141a,#8e0609);display:flex;align-items:center;font-size:8.5px;color:#fff}
.nav a{color:#fff;text-decoration:none;padding:0 20px;height:100%;display:flex;align-items:center}
.nav a.active{background:linear-gradient(180deg,#555,#2c2c2c);justify-content:center;width:78px;padding:0}
.hero-box{left:90px;top:183px;width:367px;height:160px;background:rgba(60,60,60,.6);padding:18px 14px}
.hero-box h1{font-family:"Lora",serif;font-style:italic;font-weight:700;font-size:41px;line-height:36px;color:#fff;text-transform:uppercase;letter-spacing:.5px}
.hero-box h1 em{color:#e3141b;display:block}
.hero-box p{font-size:8.3px;line-height:10.5px;color:#fff;margin-top:4px;width:300px}
.section-title{font-family:"PT Sans Narrow",sans-serif;font-weight:400;font-size:27px;color:var(--ink);letter-spacing:.5px}
.service{width:175px}
.service .photo{width:171px;height:100px;border:1px solid #ccc}
.service h3{font-family:"PT Sans Narrow",sans-serif;font-weight:400;font-size:15px;color:#333;margin-top:15px}
.service h4{font-weight:400;font-size:8.5px;color:var(--red);margin-top:2px}
.service p{font-size:7.3px;line-height:9.2px;color:#333;margin-top:4px}
.btn{display:inline-block;margin-top:17px;width:56px;height:18px;background:var(--red);color:#fff;font-size:7.5px;font-weight:700;text-align:center;line-height:18px}
.rule{left:116px;width:559px;height:2px;background:var(--line)}
.news{width:190px;display:flex;gap:6px}
.date{flex:none;width:39px;height:45px;background:#262626;color:#fff;text-align:center;font-size:8px;line-height:10px;padding-top:4px}
.date b{display:block;font-size:13px;line-height:14px}
.news p{font-size:7.3px;line-height:9px;color:#222}
.member{width:190px}
.member h4{font-weight:400;font-size:8.5px;color:var(--red)}
.member .row{display:flex;gap:9px;margin-top:3px}
.member .photo{width:77px;height:47px;border:1px solid #ccc;flex:none}
.member p{font-size:7.3px;line-height:9px;color:#222}
.footer{left:0;top:1083px;width:791px;height:117px;background:var(--footer)}
.foot-logo{left:128px;top:1122px;width:108px;height:29px;background:var(--plate);clip-path:polygon(8% 0,92% 0,100% 50%,92% 100%,8% 100%,0 50%);display:flex;align-items:center;justify-content:center}
.foot-logo .brand{font-size:8.5px}
.privacy{left:138px;top:1158px;font-family:"Lora",serif;font-style:italic;font-weight:700;font-size:9px;color:#fff}
.foot-nav{left:455px;top:1129px;font-size:8.5px;font-weight:700;color:#fff}
.foot-phone{left:458px;top:1149px;font-size:8.5px;color:#fff}
</style>
</head>
<body>
<div class="abs hero" role="img" aria-label="Photo of a woman in a blue top jogging outdoors past trees and buildings"></div>

<div class="abs logo-plate"><span class="brand">Summit Motion<br>Wellness</span></div>
<div class="abs social" aria-label="Social links"><span></span><span></span><span></span><span></span></div>
<div class="abs hours">Mon-Fri: 7.30am-7pm, Sat: 8am-2pm | <a href="#">Register</a> | <a href="#">Login</a></div>
<nav class="abs nav">
  <a class="active" href="#">HOME</a><a href="#">ABOUT US</a><a href="#">SERVICES</a><a href="#">PRODUCTS</a><a href="#">CONTACTS</a>
</nav>

<div class="abs hero-box">
  <h1>Change Your<em>Life Forever</em></h1>
  <p>Lorem ipsum dolor sit amet, consectetur adipiscing elit. Nulddg dfla eu mi varius, scelerisque sapien ac, tempodfr leo. Aenean eget pretium neque.t, consectetur adipiscing elit. Nulla eu mi varius, scelerisque sapien ac, tempodfr leo. Aenean egling</p>
</div>

<h2 class="abs section-title" style="left:115px;top:490px">OUR SERVICES</h2>
<div class="abs service" style="left:115px;top:537px">
  <div class="photo" role="img" aria-label="Physiotherapist stretching a patient's leg" style="background:linear-gradient(135deg,#6d7a8c,#c9b8a8)"></div>
  <h3>KEEPING YOU ON TRACK</h3><h4>Morbi nibh lectus, ornare non porta</h4>
  <p>Lorem ipsum dolor sit amet, consectetur adipiscing elit. Curabitur sodales a orci id pulvinar. Dsddffonec porta libero sem, quis faucibus erat ullamcorpefg r sodales.Curabitur sodales a orci id pulvinar.</p>
  <span class="btn">Read More</span>
</div>
<div class="abs service" style="left:306px;top:537px">
  <div class="photo" role="img" aria-label="Group exercise class stretching" style="background:linear-gradient(180deg,#e8ecef,#cbb9a6)"></div>
  <h3>SPECIAL PROGRAM</h3><h4>Morbi nibh lectus, ornare non porta</h4>
  <p>Lorem ipsum dolor sit amet, consectetur adipiscing elit. Curabitur sodales a orci id pulvinar. Dsddffonec porta libero sem, quis faucibus erat ullamcorpefg r sodales.Curabitur sodales a orci id pulvinar.</p>
  <span class="btn">Read More</span>
</div>
<div class="abs service" style="left:503px;top:537px">
  <div class="photo" role="img" aria-label="Woman celebrating with arms raised" style="background:linear-gradient(180deg,#fafafa,#e6dcd2)"></div>
  <h3>WEIGHT LOSS PROGRAM</h3><h4>Morbi nibh lectus, ornare non porta</h4>
  <p>Lorem ipsum dolor sit amet, consectetur adipiscing elit. Curabitur sodales a orci id pulvinar. Dsddffonec porta libero sem, quis faucibus erat ullamcorpefg r sodales.Curabitur sodales a orci id pulvinar.</p>
  <span class="btn">Read More</span>
</div>

<div class="abs rule" style="top:774px"></div>

<h2 class="abs section-title" style="left:116px;top:798px">RECENT NEWS</h2>
<div class="abs news" style="left:113px;top:846px"><div class="date"><b>23</b>Sep<br>2014</div><p>Lorem ipsum dolor sit amet, consecte-tur adipiscing elit. Curabitur sodal essa orci id pulvinar. Dsddffonec porta lopt libero sem, quis faucibus erat ullamcor-pefg r sodales.</p></div>
<div class="abs news" style="left:309px;top:846px"><div class="date"><b>23</b>Sep<br>2014</div><p>Lorem ipsum dolor sit amet, consecte-tur adipiscing elit. Curabitur sodal essa orci id pulvinar. Dsddffonec porta lopt libero sem, quis faucibus erat ullamcor-pefg r sodales.</p></div>
<div class="abs news" style="left:505px;top:846px"><div class="date"><b>23</b>Sep<br>2014</div><p>Lorem ipsum dolor sit amet, consecte-tur adipiscing elit. Curabitur sodal essa orci id pulvinar. Dsddffonec porta lopt libero sem, quis faucibus erat ullamcor-pefg r sodales.</p></div>

<div class="abs rule" style="top:921px"></div>

<h2 class="abs section-title" style="left:117px;top:942px">ABOUT OUR TEAM</h2>
<div class="abs member" style="left:120px;top:986px"><h4>Morbi nibh lectus, ornare</h4><div class="row"><div class="photo" role="img" aria-label="Portrait of team member" style="background:linear-gradient(180deg,#e9edf0,#6aa0c8)"></div><p>Lorem ipsum dolor sit amet, consec dfgrtetur adipi scsing elit. Curabi-tur sodalef essa orci id pulvinar.</p></div></div>
<div class="abs member" style="left:319px;top:986px"><h4>Morbi nibh lectus, ornare</h4><div class="row"><div class="photo" role="img" aria-label="Portrait of team member" style="background:linear-gradient(180deg,#6b6b5f,#b3403a)"></div><p>Lorem ipsum dolor sit amet, consec dfgrtetur adipi scsing elit. Curabi-tur sodalef essa orci id pulvinar.</p></div></div>
<div class="abs member" style="left:518px;top:986px"><h4>Morbi nibh lectus, ornare</h4><div class="row"><div class="photo" role="img" aria-label="Portrait of team member" style="background:linear-gradient(180deg,#f6f6f6,#e2cdbd)"></div><p>Lorem ipsum dolor sit amet, consec dfgrtetur adipi scsing elit. Curabi-tur sodalef essa orci id pulvinar.</p></div></div>

<div class="abs rule" style="top:1080px"></div>

<footer class="abs footer"></footer>
<div class="abs foot-logo"><span class="brand">Summit Motion Wellness</span></div>
<div class="abs privacy">2014 © Privacy Policy</div>
<div class="abs foot-nav">HOME | ABOUT US | SERVICES | PRODUCTS | CONTACTS</div>
<div class="abs foot-phone">Get In Touch With Us :1 800 555 01 234</div>
</body>
</html>
```